Life Coaching business needs a new flyer

We are an Australian business that specialises in Life Coaching, Career Coaching, Health and Wellness Coaching, Yoga and Pilates. We need a A4 double sided flyer that is full colour and folded to DL format. I have attached a couple of designs that I like and some pictures and would like the flyer to be bright yet stylish.

Life Coaching

```html
<!DOCTYPE html>
<html lang="en">
<head>
<meta charset="utf-8">
<title>Bright Path Coaching – DL Flyer</title>
<link href="https://fonts.googleapis.com/css2?family=Roboto:ital,wght@0,300;0,400;0,500;0,700;1,400;1,700&display=swap" rel="stylesheet">
<style>
:root{
  --bg:#d9d9d9;
  --paper:#f7f7f7;
  --blue:#1ea5e3;
  --green:#56bf2f;
  --lime:#9bd63a;
  --text:#555a5e;
  --white:#ffffff;
  --photo-warm:#e9b36c;
  --photo-sky:#6fb9e6;
  --photo-sea:#35c6d6;
}
*{box-sizing:border-box;margin:0;padding:0}
html,body{width:936px;height:1200px;overflow:hidden;background:var(--bg);font-family:'Roboto',Arial,sans-serif;color:var(--text)}
.sheet{position:absolute;left:18px;width:900px;background:var(--paper);overflow:hidden;box-shadow:0 2px 6px rgba(0,0,0,.15)}
.sheet--outside{top:16px;height:570px}
.sheet--inside{top:606px;height:578px}
.fold{position:absolute;top:0;bottom:0;width:1px;background:rgba(0,0,0,.05)}
.wave{position:absolute;left:0;bottom:0;width:900px;height:70px}
.abs{position:absolute}
.photo{position:absolute}

.brand{position:absolute;text-align:center}
.brand__dot{display:block;margin:0 auto 6px;width:46px;height:46px;border-radius:50%;background:var(--green)}
.brand__name{font-size:13px;font-weight:500;color:var(--blue);letter-spacing:.5px;line-height:1.2}

.testimonials{left:38px;top:20px;width:228px}
.testimonials h2{font-size:12px;font-weight:700;color:var(--blue);text-align:center;margin-bottom:10px}
.quote{font-size:7.6px;line-height:1.35;text-align:center;margin-bottom:10px}
.quote__mark{color:var(--lime);font-weight:700;font-size:13px;line-height:0;vertical-align:-3px}
.quote__by{display:block;text-align:right;font-size:7.6px;font-weight:700;font-style:italic;color:var(--blue);margin-top:2px}

.intro{left:320px;top:34px;width:240px;height:180px;background:linear-gradient(135deg,var(--lime),var(--green))}
.intro h2{position:absolute;left:14px;top:14px;font-size:11px;font-weight:700;color:var(--white);line-height:1.15}
.intro p{position:absolute;left:14px;top:46px;width:84px;font-size:7.4px;line-height:1.35;color:var(--white)}
.call-badge{position:absolute;left:508px;top:20px;width:62px;height:62px;border-radius:50%;background:var(--blue);color:var(--white);font-size:10px;line-height:1.1;display:flex;align-items:center;justify-content:center;text-align:center}

.offer{left:318px;top:234px;width:246px;height:76px;background:linear-gradient(90deg,var(--green),var(--lime));border-top:3px solid var(--lime);border-bottom:3px solid var(--lime);color:var(--white);text-align:center;padding-top:12px;font-size:11px;line-height:1.3}
.offer strong{font-weight:700}
.offer small{font-size:9px}

.contact{left:320px;top:334px;width:240px;text-align:center;font-size:7.6px;line-height:1.4}
.contact__phone{font-size:11px;margin:8px 0 10px}
.contact__phone b{color:var(--blue);font-weight:700}
.contact__web{color:var(--blue);font-weight:700;margin-top:8px}

.tile{position:absolute;left:610px;width:270px;height:110px}
.tile__tab{position:absolute;left:8px;top:12px;background:var(--lime);color:var(--white);font-size:10px;font-weight:500;padding:4px 10px}

.q-list{left:28px;top:130px;width:250px}
.q{font-size:13.5px;font-weight:300;color:var(--blue);line-height:1.2;margin-bottom:9px;padding-left:30px;text-indent:-30px}
.q b{font-weight:700}
.answer{font-size:13.5px;font-weight:700;color:var(--blue);margin-top:6px}

.col{position:absolute;top:126px;width:264px}
.col h3{font-size:10.5px;font-weight:700;color:var(--blue);line-height:1.1;margin:0 0 4px}
.col p{font-size:7.4px;line-height:1.35;margin-bottom:4px}
.col section{margin-bottom:12px}
.col .lead{font-weight:700;color:#333;font-size:7.6px}
.bullets{list-style:none;margin:3px 0 12px}
.bullets li{font-size:7.4px;font-weight:700;color:var(--blue);line-height:1.55;padding-left:9px;position:relative}
.bullets li::before{content:"";position:absolute;left:0;top:4px;width:4px;height:4px;border-radius:50%;background:var(--blue)}
</style>
</head>
<body>

<div class="sheet sheet--outside">
  <div class="fold" style="left:300px"></div>
  <div class="fold" style="left:600px"></div>

  <div class="abs testimonials">
    <h2>Happy Clients Testimonials</h2>
    <p class="quote"><span class="quote__mark">“</span>I have lost 10 kilos and now have the energy to play with my kids. Thanks Anna for you support/guidance and helping me get rid of my limiting beliefs. I feel I can achieve anything now! The sky's the limit.<span class="quote__mark">”</span><span class="quote__by">Mia, Mosman</span></p>
    <p class="quote"><span class="quote__mark">“</span>I had always wanted to start up own café however every time it came to putting it into practice I would procrastinate and not achieve anything. I became overwhelmed with the whole process and never achieved anything. Anna put it into bite sized chunks and helped me to set small achievable goals. I am now a happy café owner.<span class="quote__mark">”</span><span class="quote__by">Jess, Double Bay</span></p>
    <p class="quote"><span class="quote__mark">“</span>Anna has helped to change my life around in all aspects. I would have been lost without her. Thanks Anna for your professionalism, support and guidance.<span class="quote__mark">”</span><span class="quote__by">Chloe, Cremorne</span></p>
    <p class="quote"><span class="quote__mark">“</span>I was so busy with kids, work, and my husband I lost who I was. Anna has helped me find the person I am again.<span class="quote__mark">”</span><span class="quote__by">Emma, Chatswood</span></p>
    <p class="quote"><span class="quote__mark">“</span>When I started with Coach Anna, I didn't know anything about coaching. I called her because she helped a friend of mine make a career change that was a perfect fit for her. I had the opportunity to make a change too and did not know where to start. I am now in a job that I love. I would recommend Anna to everyone.<span class="quote__mark">”</span><span class="quote__by">Daniel, Texas America</span></p>
  </div>
  <div class="photo" role="img" aria-label="Photo of happy friends celebrating at sunset" style="left:22px;top:418px;width:254px;height:116px;background:linear-gradient(135deg,#f6d58a,var(--photo-warm) 55%,#8fb9d6)"></div>

  <div class="abs intro">
    <h2>Bright Path Coaching &amp;<br>Meditation Studio</h2>
    <p>Is a professional service that can help you achieve the goals that you are looking for in Life Coaching, Meditation, and Yoga/Pilates.</p>
    <div class="photo" role="img" aria-label="Photo of the two coaches" style="left:100px;top:52px;width:136px;height:128px;background:linear-gradient(180deg,#cfe9b8,#8fc36a)"></div>
  </div>
  <div class="call-badge">CALL US<br>TODAY!</div>

  <div class="abs offer"><strong>FREE</strong> Introductory Life Coaching<br>Phone/Video Call session – 20 mins<br><small>(To see if coaching is right for you)</small></div>

  <div class="abs contact">
    <p>If you are ready to take your life to the next level and would like to know more, please contact us.</p>
    <p class="contact__phone">Phone: <b>02 9000 1234</b></p>
    <p>Email: hello@brightpathstudio.com.au</p>
    <p class="contact__web">www.brightpathstudio.com.au</p>
  </div>

  <div class="brand" style="left:340px;top:426px;width:200px">
    <span class="brand__dot"></span>
    <span class="brand__name">BRIGHT PATH COACHING</span>
  </div>

  <div class="brand" style="left:640px;top:30px;width:210px">
    <span class="brand__dot"></span>
    <span class="brand__name">BRIGHT PATH COACHING</span>
  </div>

  <div class="tile" role="img" aria-label="Photo of a signpost pointing to life, balance, career, family, health and friends" style="top:120px;background:linear-gradient(180deg,var(--photo-sky),#2f7fc4)"><span class="tile__tab">Life Coaching</span></div>
  <div class="tile" role="img" aria-label="Photo of a group meditating outdoors" style="top:250px;background:linear-gradient(180deg,#5fb2e8,#9dd7f2 55%,#6ca94a)"><span class="tile__tab" style="left:auto;right:0">Meditation</span></div>
  <div class="tile" role="img" aria-label="Photo of a woman in a yoga pose by the sea" style="top:380px;background:linear-gradient(180deg,#3aa3e0,#bfe6f7)"><span class="tile__tab">Yoga/Pilates</span></div>

  <svg class="wave" viewBox="0 0 900 70" preserveAspectRatio="none" aria-hidden="true">
    <path d="M0 40 C180 20 300 55 470 45 C640 35 760 10 900 22 L900 70 L0 70Z" fill="var(--green)"/>
    <path d="M0 40 C180 20 300 55 470 45 C640 35 760 10 900 22 L900 30 C760 20 640 45 470 54 C300 62 180 32 0 48Z" fill="var(--lime)"/>
  </svg>
</div>

<div class="sheet sheet--inside">
  <div class="fold" style="left:300px"></div>
  <div class="fold" style="left:600px"></div>

  <div class="photo" role="img" aria-label="Photo of a smiling office team" style="left:0;top:0;width:150px;height:104px;background:linear-gradient(180deg,#e8eef2,#aebfcc)"></div>
  <div class="photo" role="img" aria-label="Photo of an older couple toasting" style="left:150px;top:0;width:150px;height:104px;background:linear-gradient(135deg,#f0c98a,#c98b4a)"></div>
  <div class="photo" role="img" aria-label="Photo of a swimmer in clear turquoise water" style="left:300px;top:0;width:150px;height:104px;background:linear-gradient(135deg,var(--photo-sea),#1f8fb8)"></div>
  <div class="photo" role="img" aria-label="Photo of a joyful woman beside a pink car" style="left:450px;top:0;width:150px;height:104px;background:linear-gradient(180deg,#8cc9ef,#e7668a)"></div>
  <div class="photo" role="img" aria-label="Photo of a family outdoors" style="left:600px;top:0;width:150px;height:104px;background:linear-gradient(180deg,#8fc3e0,#c9965f)"></div>
  <div class="photo" role="img" aria-label="Photo of a mother and child in sunlight" style="left:750px;top:0;width:150px;height:104px;background:linear-gradient(135deg,#f7d27a,#d98a3f)"></div>

  <div class="abs q-list">
    <p class="q"><b>Q.1</b> Are you looking at making changes this year?</p>
    <p class="q"><b>Q. 2</b> Are you stuck in a rut or at a crossroad in your life?</p>
    <p class="q"><b>Q. 3</b> Are you wanting to lose weigh but can't get motivated?</p>
    <p class="q"><b>Q. 4</b> Do you have ongoing problems with your career, relationships, or just life itself?</p>
    <p class="answer">A. Life coaching is the answer</p>
  </div>
  <div class="brand" style="left:50px;top:440px;width:200px">
    <span class="brand__dot"></span>
    <span class="brand__name">BRIGHT PATH COACHING</span>
  </div>

  <div class="col" style="left:318px">
    <section>
      <h3>Bright Path Coaching &amp;<br>Meditation Studio</h3>
      <p>Our mission is to help you become the best possible person you can be. Mentally, physically, and spiritually.</p>
      <p>We offer highly qualified and compassionate trainers/coaches for Life Coaching, Meditation, Yoga and Pilates.</p>
      <p>They will guide and motivate you every step of the way to achieve all your dreams and goals.</p>
      <p>They will make you be the best you can be.</p>
    </section>
    <section>
      <h3>Life Coaching</h3>
      <p>Your Life Coach will give you the confidence and the ability to move forward in a positive manner in all areas of your life where you crave change.</p>
      <p>Life Coaching is about breaking down the barriers preventing this change from happening, and creating the ideal environment for positive action to take place. It is a holistic approach, which looks at the present and sets goals for a totally successful future.</p>
    </section>
    <section>
      <h3>Career Coaching</h3>
      <p>Are you at a crossroads in your career and at a loss about what to do next? Do you want your work to be in alignment with the authentic you? It can be difficult to assess career options, goals, and strategies, and have the confidence to implement changes on your own. With the right coaching support, you will gain the clarity that you need to take control and have a fulfilling and rewarding career.</p>
    </section>
  </div>

  <div class="col" style="left:616px">
    <section style="margin-bottom:6px">
      <h3>Wellness Coaching</h3>
      <p>Health and wellness coaches help their clients find the motivation and tools to achieve their health and wellness goals, working with the client to examine and improve the psychological framework that supports those goals. Why Would I Need Help?</p>
      <p>Coaching is for anyone who wants to make lasting changes in their life.</p>
      <p class="lead">Coaching can assist with such issues as:</p>
      <ul class="bullets">
        <li>Creating a better work- life balance</li>
        <li>Resolving relationship issues</li>
        <li>Career guidance</li>
        <li>Stress management</li>
        <li>Weight loss and fitness</li>
        <li>Motivation and goal setting</li>
        <li>Boosting your self esteem</li>
        <li>Overcoming negative emotions and thoughts</li>
      </ul>
    </section>
    <section>
      <h3>Better time management<br>Meditation</h3>
      <p>We specialise in teaching meditation from beginners to advanced and teach a variety of techniques for stress reduction, peace of mind, stillness, and clarity.</p>
    </section>
    <section>
      <h3>Yoga/Pilates</h3>
      <p>Your highly qualified and experienced Yoga or Pilates instructor will come to you and create a fun and varied workout based on what you enjoy and what your goals are.</p>
    </section>
  </div>

  <svg class="wave" viewBox="0 0 900 70" preserveAspectRatio="none" aria-hidden="true">
    <path d="M0 28 C150 8 260 40 420 38 C600 36 720 48 900 30 L900 70 L0 70Z" fill="var(--green)"/>
    <path d="M0 28 C150 8 260 40 420 38 C600 36 720 48 900 30 L900 38 C720 56 600 44 420 46 C260 48 150 16 0 36Z" fill="var(--lime)"/>
  </svg>
</div>

</body>
</html>
```